Business card design needed

I need a business card design for a dog walking, dog minding and dog training business. Please refer to my website for the basic company colours and fonts I'm after. Planning on a double sided card, so all information doesn't need to be on the 'front' side.
Cheers

Industry/Entity Type

Dog Training

Contact Information for Business Card

Bramble Paws - guiding hounds
Ned 0487306914
bramblepawsdemo.com.au
-walking
-holiday stays
-onsite care
-training and behavioural consultations

```html
<!DOCTYPE html>
<html lang="en">
<head>
<meta charset="utf-8">
<title>Bramble Paws – Business Card</title>
<link href="https://fonts.googleapis.com/css2?family=Questrial&display=swap" rel="stylesheet">
<style>
  :root {
    --stage: #2e2e2e;
    --card-dark-top: #1a1a1a;
    --card-dark-bottom: #050505;
    --card-light: #ffffff;
    --orange: #e8651f;
    --orange-bar: #f08a24;
    --grey-logo: #8c8c8c;
    --grey-text: #4a4a4a;
    --name-light: #d8d8d8;
    --web-grey: #9a9a9a;
  }
  * { margin: 0; padding: 0; box-sizing: border-box; }
  html, body {
    width: 1200px; height: 1000px; overflow: hidden;
    background: var(--stage);
    font-family: "Questrial", Arial, sans-serif;
  }
  .canvas { position: relative; width: 1200px; height: 1000px; }

  .card { position: absolute; left: 297px; width: 616px; height: 337px; overflow: hidden; }
  .card--front { top: 162px; background: radial-gradient(ellipse at 40% 40%, var(--card-dark-top), var(--card-dark-bottom)); }
  .card--back { top: 531px; height: 336px; width: 615px; background: var(--card-light); }

  .abs { position: absolute; }

  .brand { font-size: 30px; letter-spacing: -0.5px; white-space: nowrap; line-height: 1; }
  .tagline { font-size: 9px; color: var(--orange); letter-spacing: .5px; text-transform: uppercase; white-space: nowrap; text-align: right; }

  /* front */
  .front-logo { left: 39px; top: 141px; color: var(--orange); }
  .front-tagline { left: 149px; top: 177px; width: 120px; }
  .divider { left: 309px; top: 104px; width: 1px; height: 136px; background: linear-gradient(to bottom, transparent, #3a3a3a, transparent); }
  .holder-name { left: 353px; top: 143px; font-size: 24px; color: var(--name-light); }
  .phone-bar { left: 336px; top: 175px; width: 280px; height: 18px; background: linear-gradient(to right, var(--orange-bar), var(--orange)); }
  .phone { left: 10px; top: 2px; font-size: 11px; color: #fff; letter-spacing: .5px; }
  .puppy-photo { left: 433px; top: 56px; width: 183px; height: 130px;
    background: radial-gradient(ellipse at 50% 45%, #f3ece4 0%, #c9773a 45%, transparent 72%); }
  .website { right: 15px; bottom: 10px; font-size: 12px; color: var(--web-grey); letter-spacing: 1px; }

  /* back */
  .back-logo { left: 26px; top: 132px; color: var(--grey-logo); }
  .back-tagline { left: 138px; top: 192px; width: 120px; }
  .services { left: 45px; top: 226px; list-style: none; font-size: 14.3px; line-height: 17.5px; color: var(--grey-text); letter-spacing: .3px; text-transform: uppercase; }
  .bottom-bar { left: 0; bottom: 0; width: 100%; height: 12px; background: var(--orange-bar); }
  .photo { position: absolute; }
  .photo--dogs-greeting { left: 354px; top: 6px; width: 151px; height: 113px; background: linear-gradient(to bottom, #7fa7c9, #6b7a4a 60%, #5d6b36); }
  .photo--dog-running { left: 486px; top: 69px; width: 114px; height: 193px; background: linear-gradient(to bottom, #9fb4c4, #6f8f3f 30%, #5b7d34); }
  .photo--dog-sky { left: 293px; top: 114px; width: 152px; height: 113px; background: linear-gradient(to bottom, #5f8fc8, #c9d6e0 50%, #7a6a4a); }
  .photo--dogs-field { left: 397px; top: 219px; width: 129px; height: 96px; background: linear-gradient(to bottom, #b9cde0, #6e8a45 45%, #5d7434); }
</style>
</head>
<body>
<main class="canvas">
  <section class="card card--front">
    <div class="abs brand front-logo">BRAMBLE PAWS</div>
    <div class="abs tagline front-tagline">Guiding Hounds</div>
    <div class="abs divider"></div>
    <div class="abs holder-name">Ned</div>
    <div class="abs phone-bar"><span class="abs phone">T: 0487306914</span></div>
    <div class="abs puppy-photo" role="img" aria-label="Photo of a brown and white puppy peeking over the bar"></div>
    <div class="abs website">www.bramblepawsdemo.com.au</div>
  </section>

  <section class="card card--back">
    <div class="abs brand back-logo">BRAMBLE PAWS</div>
    <div class="abs tagline back-tagline">Guiding Hounds</div>
    <ul class="abs services">
      <li>-Walking</li>
      <li>-Holiday Stays</li>
      <li>-Onsite Care</li>
      <li>-Training and Behavioural Consultations</li>
    </ul>
    <div class="photo photo--dogs-greeting" role="img" aria-label="Photo of two dogs greeting in a park"></div>
    <div class="photo photo--dog-running" role="img" aria-label="Photo of a brown dog running across a grassy field"></div>
    <div class="photo photo--dog-sky" role="img" aria-label="Photo of a shaggy dog against a cloudy sky"></div>
    <div class="photo photo--dogs-field" role="img" aria-label="Photo of several dogs in an open field"></div>
    <div class="abs bottom-bar"></div>
  </section>
</main>
</body>
</html>
```